Web page design for food business

The website is pantryloop.com.au and is an ordering website with thumbnails for purchasing high quality delicatessen products + fruit & vegetables.
The site is simple with a focus on clicking foods to buy and then pay for. There are no complicated product reviews or anything. Aside from the normal about us and contact us pages the website is essentially thumbnails for ordering and a high quality homepage to educate and showcase the business when people go to the URL.
There are 2 main tasks
The first task is a page design (i.e. header, footer, sides...) to carry through for all the pages in the website.
The second task is for the homepage specifically. I want a professional looking homepage with 3 large slide banners that look "elegant" and "artisan" as this is a deli website not a general grocery website. One slider should refer to "daily deliveries" and I will leave the other 2 sliders to your professional judgement. The homepage should also provide for room under the slide banner for specials/products of the month/etc and general promotional information
Target Market(s)
higher income earners, foodies, professionals, quality foods
Industry/Entity Type
Food Store
Number of Pages Required
2 page
Requirements
Must have
- Fresh quality food ready to be delivered
- Ease of ordering
- The feel of a high quality deli
Nice to have
- References to fresh fruit and vegetables for greenery and freshness
Should not have
- .

```html
<!DOCTYPE html>
<html lang="en">
<head>
<meta charset="utf-8">
<title>Pantryloop – Shop</title>
<link href="https://fonts.googleapis.com/css2?family=Raleway:wght@400;500;600;700&display=swap" rel="stylesheet">
<style>
:root{
  --green:#7cc242;
  --green-dark:#5fa52c;
  --ink:#333;
  --muted:#888;
  --line:#e4e4e4;
  --bg:#fff;
  --soft:#f4f4f4;
  --dark:#2b2b2b;
  --darker:#1f1f1f;
  --red:#e74c3c;
  --orange:#f5a623;
  --blue:#29b6d8;
  --star:#7cc242;
}
*{box-sizing:border-box;margin:0;padding:0}
html,body{width:747px;height:1200px;overflow:hidden}
body{font-family:"Raleway",sans-serif;color:var(--ink);background:var(--bg);position:relative;font-size:8px}
.abs{position:absolute}

/* header */
.site-header{left:0;top:0;width:747px;height:24px;background:#fff;border-bottom:1px solid var(--line)}
.brand{left:22px;top:6px;font-size:10px;font-weight:700;letter-spacing:1px;color:var(--ink)}
.main-nav{left:248px;top:8px;display:flex;gap:11px;font-size:6.5px;font-weight:700;letter-spacing:.4px}
.main-nav span.active{color:var(--green)}
.main-nav .sep{color:#bbb}
.header-icons{left:653px;top:7px;display:flex;gap:7px}

/* hero */
.hero{left:0;top:24px;width:747px;height:238px;background:radial-gradient(ellipse at 50% 60%,#5a4a3c 0%,#3a2f27 45%,#1e1a17 100%)}
.hero-title{left:0;top:42px;width:747px;text-align:center;color:#fff;font-size:30px;font-weight:500}
.hero-icon{left:364px;top:94px}
.hero-btn{left:350px;top:106px;width:46px;height:28px;background:var(--green);color:#fff;font-size:8px;font-weight:700;display:flex;align-items:center;justify-content:center}
.settings-tab{left:0;top:44px;width:18px;height:18px;background:#fff;display:flex;align-items:center;justify-content:center}
.social-rail{left:731px;top:72px;width:16px}
.social-rail i{display:block;width:16px;height:16px;margin-bottom:2px;background:var(--red)}
.social-rail i:nth-child(2){background:#d43c2e}
.social-rail i:nth-child(4){background:#c0392b}

/* breadcrumb */
.crumbs{left:0;top:262px;width:747px;height:20px;background:var(--soft);font-size:6.5px;color:var(--muted);padding:6px 0 0 56px}

/* sidebar */
.side-title{left:68px;font-size:13px;font-weight:600}
.side-rule{left:68px;width:34px;height:2px;background:var(--green)}
.cat-list{left:68px;top:354px;width:140px}
.cat{height:30px;display:flex;align-items:center;border-bottom:1px solid var(--line);font-size:8px}
.cat .ico{width:10px;height:8px;border:1.2px solid #777;border-radius:2px;margin:0 8px 0 4px}
.cat .arr{margin-left:auto;color:#999}
.swatches{left:68px;top:610px;display:grid;grid-template-columns:repeat(4,14px);gap:8px 10px}
.swatches i{width:14px;height:14px;display:block}
.price-track{left:68px;top:724px;width:120px;height:4px;background:#ddd;border-radius:2px}
.price-range{left:68px;top:724px;width:84px;height:4px;background:var(--green);border-radius:2px}
.knob{top:719px;width:14px;height:14px;border-radius:50%;background:#fff;border:1px solid #ccc}

/* toolbar */
.toolbar{left:220px;top:334px;width:456px;height:18px;border-bottom:1px solid var(--line);font-size:6.5px;color:var(--muted);display:flex;align-items:center;gap:10px}
.select{border:1px solid var(--line);padding:2px 8px;color:var(--ink)}
.view{margin-left:auto;display:flex;align-items:center;gap:3px}
.view i{width:9px;height:9px;display:block;background:#ccc}
.view i.on{background:var(--green)}

/* products */
.grid{left:220px;top:368px;width:456px;display:grid;grid-template-columns:repeat(3,146px);column-gap:9px;row-gap:14px}
.card{height:234px;border:1px solid var(--line);position:relative;text-align:center;background:#fff}
.card .photo{margin:14px auto 0;width:116px;height:90px;border-radius:4px}
.card .name{margin-top:22px;font-size:10px;font-weight:500}
.card .stars{margin-top:5px;font-size:6px;color:var(--muted);display:flex;justify-content:center;align-items:center;gap:4px}
.card .stars b{color:var(--star);letter-spacing:1px;font-size:7px}
.card .price{margin-top:9px;font-size:13px;font-weight:600}
.card .cart{margin:9px auto 0;width:64px;height:20px;background:var(--green);color:#fff;font-size:6.5px;font-weight:600;display:flex;align-items:center;justify-content:center}
.badge{position:absolute;top:-8px;right:-8px;width:26px;height:26px;border-radius:50%;color:#fff;font-size:6px;font-weight:700;display:flex;align-items:center;justify-content:center}
.b-new{background:var(--red)}.b-sale{background:var(--orange)}.b-blue{background:var(--blue)}

.pager{left:360px;top:866px;display:flex;gap:14px;font-size:8px;color:var(--ink)}
.pager .cur{color:var(--green);font-weight:700}

/* footer */
.footer{left:0;top:910px;width:747px;height:250px;background:linear-gradient(180deg,#2e2c2a,#262422)}
.f-col{top:950px;width:150px;color:#bbb;font-size:6.5px;line-height:1.6}
.f-col h3{color:#fff;font-size:16px;font-weight:600;margin-bottom:16px}
.f-col h3 span{font-weight:400}
.f-row{display:flex;align-items:center;gap:7px;margin-bottom:8px}
.f-dot{width:12px;height:12px;border-radius:50%;background:#555;flex:none}
.avatar{width:26px;height:26px;border-radius:50%;background:#7a6a5c;flex:none}
.to-top{left:357px;top:1135px;width:32px;height:22px;background:#fff;display:flex;align-items:center;justify-content:center}
.bottom-bar{left:0;top:1160px;width:747px;height:40px;background:var(--darker);color:#999;font-size:6.5px}
.bottom-bar .copy{position:absolute;left:56px;top:16px}
.bottom-bar .links{position:absolute;right:56px;top:16px;display:flex;gap:14px;color:#ccc}
</style>
</head>
<body>

<header class="abs site-header">
  <div class="abs brand">LOGO</div>
  <nav class="abs main-nav"><span>HOME</span><span>BLOG</span><span>PORTFOLIO</span><span class="sep">|</span><span class="active">SHOP</span><span>CONTACT</span></nav>
  <div class="abs header-icons">
    <svg width="9" height="9" viewBox="0 0 10 10"><circle cx="4" cy="4" r="3" fill="none" stroke="#333" stroke-width="1.3"/><line x1="6.3" y1="6.3" x2="9" y2="9" stroke="#333" stroke-width="1.3"/></svg>
    <svg width="9" height="9" viewBox="0 0 10 10"><circle cx="5" cy="5" r="4.5" fill="var(--green)"/></svg>
  </div>
</header>

<section class="abs hero" role="img" aria-label="Dimly lit plated food photograph behind the page title"></section>
<div class="abs hero-title">Birthday party</div>
<svg class="abs hero-icon" width="18" height="8" viewBox="0 0 18 8"><rect x="2" y="2" width="14" height="5" fill="none" stroke="#fff" stroke-width="1"/><line x1="0" y1="7.5" x2="18" y2="7.5" stroke="#fff"/></svg>
<div class="abs hero-btn" style="top:214px">Shop</div>
<div class="abs settings-tab"><svg width="10" height="10" viewBox="0 0 10 10"><circle cx="5" cy="5" r="3.5" fill="none" stroke="#555" stroke-width="2" stroke-dasharray="2 1.2"/><circle cx="5" cy="5" r="1.2" fill="#555"/></svg></div>
<div class="abs social-rail" style="top:74px"><i></i><i></i><i></i><i></i><i></i><i></i></div>

<div class="abs crumbs">Home &nbsp;|&nbsp; Shop &nbsp;|&nbsp; Shop page</div>

<aside>
  <div class="abs side-title" style="top:322px">Categories</div>
  <div class="abs side-rule" style="top:342px"></div>
  <div class="abs cat-list">
    <div class="cat"><i class="ico"></i>Breakfast<span class="arr">›</span></div>
    <div class="cat"><i class="ico"></i>Cakes<span class="arr">›</span></div>
    <div class="cat"><i class="ico"></i>Chocolate<span class="arr">›</span></div>
    <div class="cat"><i class="ico"></i>Cookies<span class="arr">›</span></div>
    <div class="cat"><i class="ico"></i>Dinner<span class="arr">›</span></div>
    <div class="cat"><i class="ico"></i>Drinks<span class="arr">›</span></div>
  </div>
  <div class="abs side-title" style="top:582px">Color filter</div>
  <div class="abs side-rule" style="top:602px"></div>
  <div class="abs swatches">
    <i style="background:#d9d9d9"></i><i style="background:#f4c7c7"></i><i style="background:#f5a05a"></i><i style="background:#e0e0e0"></i>
    <i style="background:#cdeaf5"></i><i style="background:#f7d4e4"></i><i style="background:#c9ecd8"></i><i style="background:#f5f0c8"></i>
  </div>
  <div class="abs side-title" style="top:690px">Price filter</div>
  <div class="abs side-rule" style="top:710px"></div>
  <div class="abs price-track"></div>
  <div class="abs price-range"></div>
  <div class="abs knob" style="left:62px"></div>
  <div class="abs knob" style="left:146px"></div>
</aside>

<div class="abs toolbar">
  <span>8 item(s)</span><span>Sort By</span><span class="select">Position ▾</span><span>Show</span><span class="select">15 ▾</span>
  <span class="view">View as <i class="on"></i><i></i></span>
</div>

<main class="abs grid">
  <div class="card"><span class="badge b-new">NEW</span><div class="photo" role="img" aria-label="Bowl of noodle salad" style="background:linear-gradient(135deg,#f2efe6,#c9b48a)"></div><div class="name">No sea takimata</div><div class="stars"><b>★★★★★</b>1 Review(s)</div><div class="price">$200.00</div><div class="cart">🛒 Add to cart</div></div>
  <div class="card"><span class="badge b-sale">SALE</span><div class="photo" role="img" aria-label="Roast chicken" style="background:linear-gradient(135deg,#f3e2c6,#b5652a)"></div><div class="name">No sea takimata</div><div class="stars"><b>★★★★★</b>1 Review(s)</div><div class="price">$200.00</div><div class="cart">🛒 Add to cart</div></div>
  <div class="card"><span class="badge b-blue">NEW</span><div class="photo" role="img" aria-label="Frosted cupcakes" style="background:linear-gradient(135deg,#f6d3e2,#b9863f)"></div><div class="name">No sea takimata</div><div class="stars"><b>★★★★★</b>1 Review(s)</div><div class="price">$200.00</div><div class="cart">🛒 Add to cart</div></div>
  <div class="card"><div class="photo" role="img" aria-label="Cooked crab" style="background:linear-gradient(135deg,#f6e6d6,#d0683a)"></div><div class="name">No sea takimata</div><div class="stars"><b>★★★★★</b>1 Review(s)</div><div class="price">$200.00</div><div class="cart">🛒 Add to cart</div></div>
  <div class="card"><div class="photo" role="img" aria-label="Burger" style="background:linear-gradient(135deg,#f2e1c2,#8a4f24)"></div><div class="name">No sea takimata</div><div class="stars"><b>★★★★★</b>1 Review(s)</div><div class="price">$200.00</div><div class="cart">🛒 Add to cart</div></div>
  <div class="card"><div class="photo" role="img" aria-label="Spoon of nuts and herbs" style="background:linear-gradient(135deg,#f4ecdd,#c69a5a)"></div><div class="name">No sea takimata</div><div class="stars"><b>★★★★★</b>1 Review(s)</div><div class="price">$200.00</div><div class="cart">🛒 Add to cart</div></div>
</main>

<nav class="abs pager"><span>«</span><span class="cur">1</span><span>2</span><span>3</span><span>4</span><span>5</span><span>»</span></nav>

<footer class="abs footer" role="img" aria-label="Dark food photograph background"></footer>
<div class="abs f-col" style="left:56px">
  <h3>Other <span>Said</span></h3>
  <div class="f-row" style="align-items:flex-start"><div class="avatar" role="img" aria-label="Customer portrait"></div><div>“Fresh produce at the door each morning, packed with real care and taste.”</div></div>
  <div style="margin-left:33px;color:#888">Marion Hale</div>
</div>
<div class="abs f-col" style="left:220px">
  <h3>Operation <span>Time</span></h3>
  <div class="f-row"><i class="f-dot"></i>Monday to Thursday: <b style="color:var(--green)">8AM – 6PM</b></div>
  <div class="f-row"><i class="f-dot"></i>Friday to Saturday: <b style="color:var(--green)">9AM – 4PM</b></div>
  <div class="f-row"><i class="f-dot"></i>Sunday: <b style="color:var(--green)">Closed</b></div>
</div>
<div class="abs f-col" style="left:384px">
  <h3>Contact <span>Us</span></h3>
  <div class="f-row"><i class="f-dot"></i>48 Larder Lane, Sydney</div>
  <div class="f-row"><i class="f-dot"></i>+61 2 8123 4470</div>
  <div class="f-row"><i class="f-dot"></i>hello@pantryloop.com.au</div>
</div>
<div class="abs f-col" style="left:546px">
  <h3>About <span>Pantryloop</span></h3>
  <div>Local deli goods, cheeses, cured meats and seasonal fruit and vegetables, hand picked and delivered fresh daily across the city to your door.</div>
</div>
<div class="abs to-top"><svg width="8" height="5" viewBox="0 0 8 5"><path d="M0 5 L4 0 L8 5Z" fill="#333"/></svg></div>
<div class="abs bottom-bar">
  <span class="copy">Design by Pantryloop · All rights reserved</span>
  <span class="links"><span>Home</span><span>Blog</span><span>Portfolio</span><span>Shop</span></span>
</div>

</body>
</html>
```